現在ホームページリニューアルを検討しております。
社内でのデザインだとどうしても前情報がある分、発想の限界、偏りがどうしてもあります。

今回はなるべくフラットな状態でデザインを検討したいと考えておりますので、こちらで公募をさせていただくことにしました。

既存の歯科医院のデザインやイメージに縛られることなく、自由な発想でご提案頂きたいと思っております。

■依頼内容

PC・スマートフォン用 それぞれ1枚 合計2枚
(実装する際にはレスポンシブの予定です。)

診療科目は
小児
一般
矯正(大学から月に数回先生にお越し頂いています)

医院の特徴
ショッピングモール内にあります
駐車場あり
バリアフリー
お子さんの遊びスペースあり
デザイナー物件

ページ数
2ページ
希望イメージ
シンプル 複雑
単色 カラフル
暗い 明るい
日常 高級
遊び心 厳粛
未来的 伝統的
女性的 男性的
納品ファイル
• 高解像度JPG (.jpg)
• フォトショップ形式 (.psd)
• PNG形式 (.png)
▼弊社が用意するもの
・ページ構成
・テキスト
・ワイヤーフレーム
・ロゴ
・写真
※受注者様のご意向があれば、ビデオ通話などで対応することも可能です。
※ページ構成や画像などは、個別に送らせていただきたいので、まずはご提案またはメッセージにてご連絡ください。

▼依頼の流れ
1.ご提案
ご提案をいただき次第、弊社よりTOPページの構成をお送りします。
3.デザイン作成
デザインを作成しましたら、提案の【追記する】からデザインファイルの追加をしてください。
5.修正依頼
修正していただきたい箇所がある場合は、修正依頼をいたしますので、修正案を再提案してください。
6.納品
フォトショップ(psd)またはイラストレーター(ai)形式で納品をしていただきます。納品が完了次第、当選を行います。

弊社では、複数のWEBサイトを運用しております。
今回はTOPページのみの依頼となっておりますが、継続的に依頼をさせていただくことも考えております。
ご提案をお待ちしております。
ワイヤーフレームと写真素材を添付します。
依頼金額を45000円に変更して、延長しました。
たくさんのご応募ありがとうございます。
現在、選考中です。3~7日程度で当選デザインを決定できるかと思いますので、今しばらくお待ちください。

歯科医院スタッフの投票にて決定いたしました。

たくさんのご提案ありがとうございます。また機会があれば、是非よろしくお願いいたします。

```html
<!DOCTYPE html>
<html lang="ja">
<head>
<meta charset="utf-8">
<title>DENTAL CLINIC</title>
<link href="https://fonts.googleapis.com/css2?family=Noto+Sans+JP:wght@300;400;500&family=Montserrat:wght@300;400;500&display=swap" rel="stylesheet">
<style>
:root{
  --blue:#3a72c2;
  --blue-dark:#2f62ad;
  --pale:#e9f0fa;
  --pale-2:#d8e4f5;
  --line:#b9cbe6;
  --text:#4a5568;
  --muted:#8a94a6;
  --orange:#ef6a2c;
  --red:#d9443a;
  --white:#fff;
}
*{box-sizing:border-box;margin:0;padding:0}
html,body{width:1200px;height:4240px;overflow:hidden}
body{font-family:"Noto Sans JP",sans-serif;font-weight:300;color:var(--text);background:var(--white);position:relative}
.en{font-family:"Montserrat",sans-serif;letter-spacing:.25em}
section,header,footer,nav{position:absolute;left:0;width:1200px}

/* header */
.site-header{top:0;height:120px}
.logo{position:absolute;left:70px;top:38px;font-size:24px;color:var(--blue);font-weight:400}
.tel{position:absolute;left:505px;top:10px;color:var(--blue)}
.tel-num{font-size:26px;font-weight:400;display:flex;align-items:center;gap:10px}
.tel-hours{font-size:13px;line-height:1.5;margin-top:4px;display:flex;gap:14px}
.btn-reserve{position:absolute;left:808px;top:40px;width:110px;height:36px;border:1px solid var(--red);color:var(--red);font-size:14px;display:flex;align-items:center;justify-content:center;letter-spacing:.1em}
.btn-web{position:absolute;left:935px;top:22px;width:170px;height:60px;background:var(--orange);color:#fff;font-size:16px;display:flex;align-items:center;justify-content:center;gap:8px;letter-spacing:.1em}

/* hero */
.hero{top:100px;height:510px}
.hero-photo{position:absolute;left:120px;top:0;width:1080px;height:510px;background:linear-gradient(90deg,#f4f6f9 0%,#eef1f5 45%,#d9dee4 75%,#c9ced6 100%)}
.hero-copy{position:absolute;left:240px;top:300px;color:var(--blue)}
.hero-copy .ja{font-size:22px;letter-spacing:.2em;font-weight:400}
.hero-copy .en{font-size:22px;margin-top:48px;letter-spacing:.35em}
.side-tab{position:absolute;left:0;top:180px;width:52px;height:320px;background:var(--blue);color:#fff;display:flex;flex-direction:column;align-items:center;padding-top:30px;gap:24px}
.side-tab span{writing-mode:vertical-rl;font-size:14px;letter-spacing:.3em}

/* nav */
.global-nav{top:620px;height:60px;display:flex;justify-content:center;gap:0}
.global-nav a{width:120px;text-align:center;text-decoration:none;color:var(--text);font-size:13px;border-left:1px solid var(--line);line-height:1.5;padding-top:6px}
.global-nav a:last-child{border-right:1px solid var(--line)}
.global-nav small{display:block;font-size:10px;color:var(--muted);font-family:"Montserrat",sans-serif;letter-spacing:.2em}

/* headings */
.sec-title{text-align:center;color:var(--text)}
.sec-title .ja{font-size:20px;letter-spacing:.3em;font-weight:400}
.sec-title .en{font-size:12px;margin-top:6px;color:var(--muted)}

/* menu */
.menu{top:700px;height:1460px}
.menu-bg{position:absolute;left:80px;top:0;width:1020px;height:1460px;background:var(--pale)}
.menu .sec-title{position:absolute;left:0;width:1200px;top:70px}
.menu-grid{position:absolute;left:220px;top:180px;display:grid;grid-template-columns:repeat(3,240px);gap:12px 20px}
.menu-card{width:240px;height:380px;background:#fff;border:2px solid var(--pale-2);padding:10px}
.menu-photo{height:210px}
.menu-card h3{font-size:14px;font-weight:400;text-align:center;margin-top:16px;letter-spacing:.1em}
.menu-card h3::after{content:"";display:block;width:40px;height:2px;background:var(--blue);margin:8px auto 0}
.menu-card p{font-size:11px;line-height:1.7;margin-top:12px;padding:0 6px}
.ph-a{background:linear-gradient(135deg,#cfe0ee,#8fb3cf)}
.ph-b{background:linear-gradient(135deg,#f1c6b4,#d98a78)}
.ph-c{background:linear-gradient(135deg,#e8edf2,#b6c6d6)}
.ph-d{background:linear-gradient(135deg,#c7d7e6,#6d8fae)}
.ph-e{background:linear-gradient(135deg,#d6e2ea,#9ab3c6)}

/* concept */
.concept{top:2220px;height:540px}
.concept-photo{position:absolute;inset:0;background:linear-gradient(120deg,#eef3f6 0%,#cdd9e2 40%,#e4ebf0 70%,#c3d1dc 100%)}
.concept .sec-title{position:absolute;left:0;width:1200px;top:80px}
.concept-cards{position:absolute;left:215px;top:180px;display:flex;gap:30px}
.concept-card{width:240px;height:210px;background:rgba(255,255,255,.45);border:1px solid rgba(255,255,255,.8);position:relative;padding:50px 22px 0}
.concept-num{position:absolute;top:-18px;left:0;width:100%;text-align:center;font-size:40px;font-style:italic;color:var(--muted);font-family:"Montserrat",sans-serif;font-weight:300}
.concept-card h3{font-size:15px;font-weight:400;color:var(--text);letter-spacing:.15em}
.concept-card p{font-size:11px;line-height:1.7;margin-top:14px}

/* news */
.news{top:2780px;height:540px}
.news-box{position:absolute;left:140px;top:0;width:920px;height:540px;border:2px solid var(--pale-2);background:#fff}
.news-head{position:absolute;left:60px;top:60px}
.news-head .ja{font-size:18px;letter-spacing:.25em;font-weight:400}
.news-head .en{font-size:12px;color:var(--muted);margin-top:4px}
.news-head p{font-size:12px;line-height:1.8;margin-top:22px;width:200px}
.btn-more{display:block;margin-top:20px;width:200px;height:40px;border:1px solid var(--line);text-align:center;line-height:38px;font-size:13px;color:var(--text);text-decoration:none}
.news-list{position:absolute;left:340px;top:30px;width:540px;list-style:none}
.news-list li{height:80px;border-bottom:1px solid var(--pale-2);padding:14px 0 0 40px;position:relative}
.news-list time{font-size:12px;font-family:"Montserrat",sans-serif;display:block}
.news-list span{font-size:13px;display:block;margin-top:6px}
.news-list svg{position:absolute;right:10px;top:26px}

/* greeting */
.greeting{top:3400px;height:460px}
.greeting-photo{position:absolute;left:0;top:0;width:1075px;height:460px;background:linear-gradient(100deg,#f3f5f2 0%,#dfe6e3 40%,#f0f2ef 70%,#d4ddd9 100%)}
.greeting-copy{position:absolute;left:120px;top:130px;width:480px}
.greeting-copy .ja{font-size:20px;letter-spacing:.3em;font-weight:400}
.greeting-copy .en{font-size:12px;color:var(--muted);margin-top:4px}
.greeting-copy p{font-size:13px;line-height:2;margin-top:26px}

/* footer */
.site-footer{top:3940px;height:300px;background:var(--blue);color:#fff}
.footer-logo{position:absolute;left:130px;top:60px;font-size:22px;font-weight:400}
.footer-tel{position:absolute;left:130px;top:110px;font-size:20px;display:flex;gap:8px;align-items:center}
.footer-hours{position:absolute;left:130px;top:148px;font-size:12px;line-height:1.7}
.footer-nav{position:absolute;left:520px;top:55px;display:flex}
.footer-nav a{width:110px;color:#fff;text-decoration:none;font-size:13px;text-align:center;border-left:1px solid rgba(255,255,255,.5);line-height:1.5}
.footer-nav a:last-child{border-right:1px solid rgba(255,255,255,.5)}
.footer-nav small{display:block;font-size:10px;font-family:"Montserrat",sans-serif;letter-spacing:.2em}
.footer-web{position:absolute;left:630px;top:170px;width:150px;height:44px;background:#fff;color:var(--blue);font-size:14px;display:flex;align-items:center;justify-content:center;letter-spacing:.1em}
.copyright{position:absolute;left:0;width:1200px;bottom:20px;text-align:center;font-size:11px;letter-spacing:.1em}
</style>
</head>
<body>

<header class="site-header">
  <div class="logo en">DENTAL CLINIC</div>
  <div class="tel">
    <div class="tel-num">
      <svg width="20" height="20" viewBox="0 0 24 24"><path fill="#3a72c2" d="M6.6 10.8c1.4 2.8 3.8 5.1 6.6 6.6l2.2-2.2c.3-.3.7-.4 1-.2 1.1.4 2.3.6 3.6.6.6 0 1 .4 1 1V20c0 .6-.4 1-1 1C10.6 21 3 13.4 3 4c0-.6.4-1 1-1h3.5c.6 0 1 .4 1 1 0 1.3.2 2.5.6 3.6.1.3 0 .7-.2 1z"/></svg>
      <span class="en" style="letter-spacing:.05em">000-0000-0000</span>
    </div>
    <div class="tel-hours"><span>診療受付時間</span><span>月〜金 10:00〜14:00<br>土 10:00〜17:00</span></div>
  </div>
  <div class="btn-reserve">診療予約</div>
  <div class="btn-web">
    <svg width="16" height="16" viewBox="0 0 16 16"><rect x="1" y="3" width="14" height="12" fill="none" stroke="#fff"/><line x1="1" y1="6" x2="15" y2="6" stroke="#fff"/></svg>
    WEB予約
  </div>
</header>

<section class="hero">
  <div class="hero-photo" role="img" aria-label="頬に手を添えて微笑む女性の写真"></div>
  <div class="hero-copy">
    <div class="ja">痛くない歯科治療</div>
    <div class="en">DENTAL CLINIC</div>
  </div>
  <div class="side-tab">
    <span>診療のご予約・お問合せ</span>
    <svg width="20" height="20" viewBox="0 0 20 20"><circle cx="10" cy="10" r="9" fill="none" stroke="#fff"/><path d="M8 6l4 4-4 4" fill="none" stroke="#fff"/></svg>
  </div>
</section>

<nav class="global-nav">
  <a href="#">当院について<small>CONCEPT</small></a>
  <a href="#">ごあいさつ<small>GREETING</small></a>
  <a href="#">診療案内<small>MENU</small></a>
  <a href="#">お知らせ<small>NEWS</small></a>
  <a href="#">お問い合わせ<small>CONTACT</small></a>
</nav>

<section class="menu">
  <div class="menu-bg"></div>
  <div class="sec-title"><div class="ja">診療案内</div><div class="en">MENU</div></div>
  <div class="menu-grid">
    <article class="menu-card"><div class="menu-photo ph-a" role="img" aria-label="レントゲン写真を見る歯科医の手元"></div><h3>治療の内容を入る</h3><p>治療内容の説明文が入ります。治療内容の説明文が入ります。治療内容の説明文。</p></article>
    <article class="menu-card"><div class="menu-photo ph-b" role="img" aria-label="矯正装置をつけた歯の写真"></div><h3>治療の内容を入る</h3><p>治療内容の説明文が入ります。治療内容の説明文が入ります。治療内容の説明文。</p></article>
    <article class="menu-card"><div class="menu-photo ph-c" role="img" aria-label="子どもを診察する歯科医の写真"></div><h3>治療の内容を入る</h3><p>治療内容の説明文が入ります。治療内容の説明文が入ります。治療内容の説明文。</p></article>
    <article class="menu-card"><div class="menu-photo ph-d" role="img" aria-label="歯の治療中の様子"></div><h3>治療の内容を入る</h3><p>治療内容の説明文が入ります。治療内容の説明文が入ります。治療内容の説明文。</p></article>
    <article class="menu-card"><div class="menu-photo ph-b" role="img" aria-label="口元の治療の様子"></div><h3>治療の内容を入る</h3><p>治療内容の説明文が入ります。治療内容の説明文が入ります。治療内容の説明文。</p></article>
    <article class="menu-card"><div class="menu-photo ph-e" role="img" aria-label="歯科器具の写真"></div><h3>治療の内容を入る</h3><p>治療内容の説明文が入ります。治療内容の説明文が入ります。治療内容の説明文。</p></article>
    <article class="menu-card"><div class="menu-photo ph-a" role="img" aria-label="レントゲン写真を見る歯科医の手元"></div><h3>治療の内容を入る</h3><p>治療内容の説明文が入ります。治療内容の説明文が入ります。治療内容の説明文。</p></article>
    <article class="menu-card"><div class="menu-photo ph-c" role="img" aria-label="子どもを診察する歯科医の写真"></div><h3>治療の内容を入る</h3><p>治療内容の説明文が入ります。治療内容の説明文が入ります。治療内容の説明文。</p></article>
    <article class="menu-card"><div class="menu-photo ph-b" role="img" aria-label="矯正装置をつけた歯の写真"></div><h3>治療の内容を入る</h3><p>治療内容の説明文が入ります。治療内容の説明文が入ります。治療内容の説明文。</p></article>
  </div>
</section>

<section class="concept">
  <div class="concept-photo" role="img" aria-label="歯科ユニットと器具の写真"></div>
  <div class="sec-title"><div class="ja">コンセプト</div><div class="en">CONCEPT</div></div>
  <div class="concept-cards">
    <div class="concept-card"><div class="concept-num">1</div><h3>コンセプト1</h3><p>コンセプトの説明文が入ります。コンセプトの説明文が入ります。</p></div>
    <div class="concept-card"><div class="concept-num">2</div><h3>コンセプト2</h3><p>コンセプトの説明文が入ります。コンセプトの説明文が入ります。</p></div>
    <div class="concept-card"><div class="concept-num">3</div><h3>コンセプト3</h3><p>コンセプトの説明文が入ります。コンセプトの説明文が入ります。</p></div>
  </div>
</section>

<section class="news">
  <div class="news-box">
    <div class="news-head">
      <div class="ja">お知らせ</div><div class="en">NEWS</div>
      <p>テキストテキストテキストテキストテキスト</p>
      <a class="btn-more" href="#">一覧を見る</a>
    </div>
    <ul class="news-list">
      <li><time>2019.10.15</time><span>タイトルタイトルタイトルタイトル</span><svg width="22" height="22" viewBox="0 0 22 22"><circle cx="11" cy="11" r="11" fill="#3a72c2"/><path d="M9 7l4 4-4 4" fill="none" stroke="#fff" stroke-width="1.5"/></svg></li>
      <li><time>2019.10.15</time><span>タイトルタイトルタイトルタイトル</span><svg width="22" height="22" viewBox="0 0 22 22"><circle cx="11" cy="11" r="11" fill="#3a72c2"/><path d="M9 7l4 4-4 4" fill="none" stroke="#fff" stroke-width="1.5"/></svg></li>
      <li><time>2019.10.15</time><span>タイトルタイトルタイトルタイトル</span><svg width="22" height="22" viewBox="0 0 22 22"><circle cx="11" cy="11" r="11" fill="#3a72c2"/><path d="M9 7l4 4-4 4" fill="none" stroke="#fff" stroke-width="1.5"/></svg></li>
      <li><time>2019.10.15</time><span>タイトルタイトルタイトルタイトル</span><svg width="22" height="22" viewBox="0 0 22 22"><circle cx="11" cy="11" r="11" fill="#3a72c2"/><path d="M9 7l4 4-4 4" fill="none" stroke="#fff" stroke-width="1.5"/></svg></li>
      <li><time>2019.10.15</time><span>タイトルタイトルタイトルタイトル</span><svg width="22" height="22" viewBox="0 0 22 22"><circle cx="11" cy="11" r="11" fill="#3a72c2"/><path d="M9 7l4 4-4 4" fill="none" stroke="#fff" stroke-width="1.5"/></svg></li>
      <li><time>2019.10.15</time><span>タイトルタイトルタイトルタイトル</span><svg width="22" height="22" viewBox="0 0 22 22"><circle cx="11" cy="11" r="11" fill="#3a72c2"/><path d="M9 7l4 4-4 4" fill="none" stroke="#fff" stroke-width="1.5"/></svg></li>
    </ul>
  </div>
</section>

<section class="greeting">
  <div class="greeting-photo" role="img" aria-label="明るい診療室の写真"></div>
  <div class="greeting-copy">
    <div class="ja">ごあいさつ</div><div class="en">GREETING</div>
    <p>ごあいさつの文章が入ります。ごあいさつの文章が入ります。ごあいさつの文章が入ります。ごあいさつの文章が入ります。ごあいさつの文章が入ります。ごあいさつの文章が入ります。</p>
  </div>
</section>

<footer class="site-footer">
  <div class="footer-logo en">DENTAL CLINIC</div>
  <div class="footer-tel">
    <svg width="18" height="18" viewBox="0 0 24 24"><path fill="#fff" d="M6.6 10.8c1.4 2.8 3.8 5.1 6.6 6.6l2.2-2.2c.3-.3.7-.4 1-.2 1.1.4 2.3.6 3.6.6.6 0 1 .4 1 1V20c0 .6-.4 1-1 1C10.6 21 3 13.4 3 4c0-.6.4-1 1-1h3.5c.6 0 1 .4 1 1 0 1.3.2 2.5.6 3.6.1.3 0 .7-.2 1z"/></svg>
    <span class="en" style="letter-spacing:.05em">000-0000-0000</span>
  </div>
  <div class="footer-hours">診療受付時間 月〜金 10:00〜14:00<br>土 10:00〜17:00</div>
  <nav class="footer-nav">
    <a href="#">当院について<small>CONCEPT</small></a>
    <a href="#">ごあいさつ<small>GREETING</small></a>
    <a href="#">診療案内<small>MENU</small></a>
    <a href="#">お知らせ<small>NEWS</small></a>
    <a href="#">お問い合わせ<small>CONTACT</small></a>
  </nav>
  <div class="footer-web">WEB予約</div>
  <div class="copyright en">Copyright© DENTAL CLINIC All Rights Reserved.</div>
</footer>

</body>
</html>
```